Stationary for Logistics Co.
Brevin Haulage Group
Project: Stationary for Logistics Co.
Stationary for Logistics Co.  - Transportation
Creative Brief
Professional
Colin Dartley
Director of Sales
4215 Marlow Ln. Cincinnati, Ohio 45239
513.620.5174 Ext. 37
colindartley@brevinhaul.example
www.brevinhaul.example
brevinhaul brevinhaul
We need business card, letterhead and envelope design. Thanks

```html
<!DOCTYPE html>
<html lang="en">
<head>
<meta charset="utf-8">
<title>Brevin Haulage Group – Business Card</title>
<link href="https://fonts.googleapis.com/css2?family=Arimo:wght@400;700&display=swap" rel="stylesheet">
<style>
  :root {
    --backdrop: #d9d9db;
    --paper: #ffffff;
    --navy: #1f3a8a;
    --red: #b3171f;
    --ink: #1f3a8a;
    --muted: #5a5f6b;
  }
  html, body {
    margin: 0;
    width: 1200px;
    height: 902px;
    overflow: hidden;
    background: var(--backdrop);
    font-family: "Arimo", Arial, sans-serif;
  }
  .canvas {
    position: relative;
    width: 1200px;
    height: 902px;
  }
  .card {
    position: absolute;
    left: 250px;
    width: 700px;
    height: 400px;
    background: var(--paper);
    box-shadow: 0 4px 14px rgba(0,0,0,0.18);
    overflow: hidden;
  }
  .card--front { top: 34px; }
  .card--back { top: 468px; }

  .lockup {
    position: absolute;
    display: flex;
    align-items: center;
    gap: 16px;
  }
  .lockup__mark {
    width: 64px;
    height: 64px;
    border-radius: 50%;
    background: var(--navy);
    flex: none;
  }
  .lockup__name {
    font-weight: 700;
    font-size: 32px;
    color: var(--ink);
    line-height: 1;
    letter-spacing: -0.3px;
    white-space: nowrap;
  }
  .lockup__rule {
    height: 2px;
    background: var(--navy);
    margin: 6px 0 5px;
  }
  .lockup__tagline {
    font-size: 17px;
    color: var(--muted);
    letter-spacing: 0.4px;
    white-space: nowrap;
  }
  .card--front .lockup { left: 155px; top: 158px; }
  .card--back .lockup { left: 34px; top: 186px; gap: 14px; }
  .card--back .lockup__mark { width: 46px; height: 46px; }
  .card--back .lockup__name { font-size: 20px; }
  .card--back .lockup__rule { margin: 5px 0 4px; }
  .card--back .lockup__tagline { font-size: 11px; letter-spacing: 0.3px; }

  .card__bg {
    position: absolute;
    inset: 0;
  }
  .contact {
    position: absolute;
    right: 40px;
    top: 48px;
    text-align: right;
    color: #fff;
  }
  .contact__name {
    font-weight: 700;
    font-size: 21px;
  }
  .contact__title {
    font-size: 16px;
    margin-top: 4px;
  }
  .contact__list {
    list-style: none;
    margin: 36px 0 0;
    padding: 0;
    font-size: 14px;
    line-height: 24px;
  }
  .contact__list li {
    display: flex;
    justify-content: flex-end;
    align-items: center;
    gap: 8px;
  }
  .icon { width: 14px; height: 14px; flex: none; }
  .icon-space { width: 14px; flex: none; }
</style>
</head>
<body>
<main class="canvas">

  <section class="card card--front" aria-label="Card front">
    <div class="lockup">
      <span class="lockup__mark" aria-hidden="true"></span>
      <div>
        <div class="lockup__name">Brevin Haulage Group</div>
        <div class="lockup__rule"></div>
        <div class="lockup__tagline">Freight Management Solutions</div>
      </div>
    </div>
  </section>

  <section class="card card--back" aria-label="Card back">
    <svg class="card__bg" viewBox="0 0 700 400" width="700" height="400" aria-hidden="true">
      <path d="M320,0 H700 V400 H260 C380,320 410,120 320,0 Z" fill="var(--navy)"/>
      <path d="M260,400 C380,320 410,120 320,0 C430,110 440,300 340,400 Z" fill="var(--red)"/>
    </svg>

    <div class="lockup">
      <span class="lockup__mark" aria-hidden="true"></span>
      <div>
        <div class="lockup__name">Brevin Haulage Group</div>
        <div class="lockup__rule"></div>
        <div class="lockup__tagline">Freight Management Solutions</div>
      </div>
    </div>

    <div class="contact">
      <div class="contact__name">Colin Dartley</div>
      <div class="contact__title">Director of Sales</div>
      <ul class="contact__list">
        <li>4215 Marlow Ln.<span class="icon-space"></span></li>
        <li>Cincinnati, OH 45239<span class="icon-space"></span></li>
        <li>513.620.5174 Ext. 37
          <svg class="icon" viewBox="0 0 24 24" aria-hidden="true"><path fill="#fff" d="M6.6 10.8a15.1 15.1 0 0 0 6.6 6.6l2.2-2.2c.3-.3.7-.4 1-.2 1.1.4 2.3.6 3.6.6.6 0 1 .4 1 1V20c0 .6-.4 1-1 1A17 17 0 0 1 3 4c0-.6.4-1 1-1h3.5c.6 0 1 .4 1 1 0 1.3.2 2.5.6 3.6.1.3 0 .7-.2 1z"/></svg>
        </li>
        <li>513.620.5174
          <svg class="icon" viewBox="0 0 24 24" aria-hidden="true"><path fill="#fff" d="M6 3h9v5H6zM4 9h16a1 1 0 0 1 1 1v7h-3v4H6v-4H3v-7a1 1 0 0 1 1-1zm4 8v2h8v-2z"/></svg>
        </li>
        <li>colindartley@brevinhaul.example
          <svg class="icon" viewBox="0 0 24 24" aria-hidden="true"><path fill="#fff" d="M3 5h18v14H3zm2 2v.5l7 4.5 7-4.5V7z"/></svg>
        </li>
        <li>www.brevinhaul.example<span class="icon-space"></span></li>
      </ul>
    </div>
  </section>

</main>
</body>
</html>
```